Flyer need for startup recruiting company

Please see the instructions page here:

https://www.filevessel.example/share/q47kd2mxt9pla8wzr3cv5/h?key=7mhs2pqx9vtn4kd8wr3lzc6bf&v=0

```html
<!DOCTYPE html>
<html lang="en">
<head>
<meta charset="utf-8">
<title>HireHelix – Recruiting Flyer</title>
<link rel="stylesheet" href="https://fonts.googleapis.com/css2?family=Montserrat:wght@400;500;700;800&display=swap">
<style>
:root{
  --backdrop:#c3c1c2;
  --paper:#ffffff;
  --ink:#1f2430;
  --dark:#23262f;
  --yellow:#f3c13f;
  --gold:#ffc107;
  --orange:#f0a044;
  --panel:#dcdcdc;
  --photo-a:#8fb4d6;
  --photo-b:#c99a62;
}
*{box-sizing:border-box;margin:0;padding:0}
html,body{width:938px;height:1200px;overflow:hidden}
body{background:var(--backdrop);font-family:"Montserrat",sans-serif;color:var(--ink);position:relative}
.flyer{position:absolute;left:85px;top:42px;width:769px;height:1085px;background:var(--paper);overflow:hidden}
.hero{position:absolute;left:0;top:0;width:769px;height:452px;
  background:linear-gradient(180deg,#e9eef3 0%,var(--photo-a) 45%,#6f8db0 62%,var(--photo-b) 85%,#a8743e 100%)}
.hero-shapes{position:absolute;left:0;top:0}
.brand{position:absolute;left:30px;top:58px;display:flex;align-items:center;gap:10px;
  font-weight:700;font-size:23px;color:var(--dark)}
.brand-dot{width:22px;height:22px;border-radius:50%;background:var(--dark)}
.headline-top{position:absolute;left:11px;top:321px;width:591px;height:52px;background:var(--yellow);
  font-weight:800;font-size:27px;line-height:52px;padding-left:9px;color:var(--dark);white-space:nowrap}
.headline-bottom{position:absolute;left:44px;top:366px;width:233px;height:47px;background:var(--dark);
  font-weight:800;font-size:27px;line-height:47px;padding-left:19px;color:#fff}
.intro{position:absolute;left:35px;top:468px;width:275px}
.intro-name{font-weight:700;font-size:26px;line-height:30px;color:#111}
.intro-text{font-size:15px;line-height:18.4px;font-weight:400;margin-top:4px;color:#1a2233}
.badge{position:absolute;left:315px;top:472px;width:123px;height:123px;background:var(--gold);border-radius:16px;text-align:center;color:#111}
.badge-num{font-weight:800;font-size:48px;line-height:52px;margin-top:12px}
.badge-months{font-weight:800;font-size:25px;line-height:26px}
.badge-word{font-weight:400;font-size:19px;line-height:22px}
.badge-pointer{position:absolute;left:50%;bottom:-13px;margin-left:-12px;width:0;height:0;
  border-left:12px solid transparent;border-right:12px solid transparent;border-top:14px solid var(--gold)}
.badge-shadow{position:absolute;left:350px;top:610px;width:52px;height:8px;border-radius:50%;background:#d8d8d8}
.pricing{position:absolute;left:452px;top:466px;width:298px;height:145px;background:var(--panel);
  padding:11px 10px 0 10px;font-size:14.6px;line-height:18.5px;text-align:justify;color:#1a2233}
.pricing b{font-weight:700}
.pricing-bar{position:absolute;left:470px;top:611px;width:280px;height:6px;background:var(--orange)}
.level{position:absolute;top:688px;width:127px;height:124px;background:var(--panel);
  box-shadow:4px 2px 0 var(--orange);text-align:center;padding:36px 1px 0;
  font-size:7.4px;line-height:9.2px;color:#333;white-space:nowrap}
.level b{font-weight:700;font-size:8.2px}
.level-mark{position:absolute;left:50%;top:-22px;margin-left:-25px;width:50px;height:50px;border-radius:50%;
  background:#fff;border:5px solid var(--orange);display:flex;flex-direction:column;align-items:center;justify-content:center;color:#111}
.level-mark small{font-size:7px;font-weight:500;line-height:8px}
.level-mark span{font-size:17px;font-weight:800;line-height:17px}
.results{position:absolute;left:36px;top:837px}
.results h2{font-size:16px;font-weight:700;line-height:20px;color:#1a2233}
.results ul{list-style:none;margin-top:0}
.results li{font-size:14.2px;line-height:18.5px;display:flex;align-items:center;gap:9px;padding-left:9px;white-space:nowrap}
.results svg{flex:none}
.closing{position:absolute;left:420px;top:839px;width:314px;font-size:14.2px;line-height:18.5px;text-align:justify;color:#1a2233}
.footer-shapes{position:absolute;left:0;top:0}
.contact-left{position:absolute;left:24px;top:1029px;font-size:14.5px;line-height:21px;color:#1a2233;font-style:normal}
.contact-left div{display:flex;align-items:center;gap:8px}
.contact-left .web{font-weight:700}
.contact-right{position:absolute;right:26px;top:1028px;text-align:right;color:#fff;font-style:normal}
.phone{display:flex;align-items:center;justify-content:flex-end;gap:8px;font-weight:700;font-size:17px;line-height:24px}
.address{font-size:13.4px;line-height:20px;margin-top:1px}
</style>
</head>
<body>
<main class="flyer">
  <div class="hero" role="img" aria-label="Photo of a sales team high-fiving around a meeting table in front of a screen with charts"></div>
  <svg class="hero-shapes" width="769" height="452" viewBox="0 0 769 452">
    <polygon points="0,0 372,0 295,29 0,189" fill="var(--yellow)"/>
    <polygon points="372,0 769,0 769,112 608,76 295,29" fill="var(--dark)"/>
    <polygon points="608,76 769,112 769,216" fill="var(--orange)"/>
  </svg>
  <div class="brand"><span class="brand-dot"></span>HireHelix</div>
  <h1 class="headline-top">Recruiting the BEST sales professionals</h1>
  <div class="headline-bottom">is in our DNA</div>

  <section class="intro">
    <h2 class="intro-name">HireHelix</h2>
    <p class="intro-text">is an advanced recruiting service company that specializes in recruiting professional sales people and sales management professionals using proven psychological testing assessments that guarantee a top performer 92% of the time.</p>
  </section>

  <div class="badge">
    <div class="badge-num">6</div>
    <div class="badge-months">Months</div>
    <div class="badge-word">Guarantee</div>
    <span class="badge-pointer"></span>
  </div>
  <div class="badge-shadow"></div>

  <p class="pricing"><b>25 years</b> of experience and flat rate pricing. Half the cost or more of the traditional contingency model. Also, our 6 month guarantee does not end with the replacement so there is <b>zero risk</b> for the customer</p>
  <div class="pricing-bar"></div>

  <div class="level" style="left:36px">
    <div class="level-mark"><small>Level</small><span>1</span></div>
    B2C In home sales<br>professionals<br>Windows, roofs, solar,<br>gutters, flooring etc<br>$6,000 with a two candidate<br>retainer minimum<br>Save $12,000 over<br>contingency model<br><b>($18,000)</b>
  </div>
  <div class="level" style="left:180px">
    <div class="level-mark"><small>Level</small><span>2</span></div>
    B2B Account Manger (80%<br>Account Mgr, 20% Hunter<br>Inside Sales, SaaS, Outside<br>sales, etc<br>$12,000 with a two candidate<br>retainer minimum<br>Save $13,000 over<br>contingency model<br><b>($25,000)</b>
  </div>
  <div class="level" style="left:323px">
    <div class="level-mark"><small>Level</small><span>3</span></div>
    B2B Business Development<br>Pro. Hunter<br>$15,000 with a two candidate<br>retainer minimum<br>Save $15,000 over<br>contingency model<br><b>($30,000)</b>
  </div>
  <div class="level" style="left:469px">
    <div class="level-mark"><small>Level</small><span>4</span></div>
    B2B &amp; B2C Sales Managers<br>$17,000 with a one candidate<br>retainer minimum<br>Save $18,000 over<br>contingency model<br><b>($35,000)</b>
  </div>
  <div class="level" style="left:618px">
    <div class="level-mark"><small>Level</small><span>5</span></div>
    B2B &amp; B2C VP of Sales,<br>CRO, CSO<br>$19,000 with<br>a one candidate retainer<br>minimum<br>Save $41,000 over<br>contingency model<br><b>($60,000)</b>
  </div>

  <svg class="footer-shapes" width="769" height="1085" viewBox="0 0 769 1085">
    <polygon points="0,969 150,1005 360,986 410,1042 769,905 769,1085 0,1085" fill="var(--yellow)"/>
    <polygon points="150,1005 360,986 410,1042 560,1030" fill="var(--orange)"/>
    <polygon points="490,1040 592,946 660,980" fill="var(--orange)"/>
    <polygon points="647,975 769,876 769,948 700,990" fill="var(--yellow)"/>
    <polygon points="0,912 124,995 0,969" fill="var(--dark)"/>
    <polygon points="388,1085 499,1025 700,990 769,948 769,1085" fill="var(--dark)"/>
  </svg>

  <section class="results">
    <h2>Our results deliver:</h2>
    <ul>
      <li><svg width="13" height="12" viewBox="0 0 13 12"><path d="M1 7l3.5 4L12 1" fill="none" stroke="#333" stroke-width="1.6"/></svg>50% Faster time to hire</li>
      <li><svg width="13" height="12" viewBox="0 0 13 12"><path d="M1 7l3.5 4L12 1" fill="none" stroke="#333" stroke-width="1.6"/></svg>96% Of wrong hires eliminated</li>
      <li><svg width="13" height="12" viewBox="0 0 13 12"><path d="M1 7l3.5 4L12 1" fill="none" stroke="#333" stroke-width="1.6"/></svg>83% New hire retention beyond the one year</li>
      <li><svg width="13" height="12" viewBox="0 0 13 12"><path d="M1 7l3.5 4L12 1" fill="none" stroke="#333" stroke-width="1.6"/></svg>50% Lower employee turnover</li>
    </ul>
  </section>
  <p class="closing">With 25+ years experience, we do the heavy lifting so you can focus on your core business. You get our seal of approval that your candidate is in the top 10%.</p>

  <address class="contact-left">
    <div><svg width="13" height="10" viewBox="0 0 13 10"><rect width="13" height="10" rx="1" fill="#1a2233"/><path d="M1 1l5.5 4.5L12 1" fill="none" stroke="var(--yellow)" stroke-width="1.2"/></svg>companyname@mailbox.example</div>
    <div class="web"><svg width="14" height="14" viewBox="0 0 14 14"><g fill="none" stroke="#1a2233" stroke-width="1.1"><circle cx="7" cy="7" r="6"/><ellipse cx="7" cy="7" rx="2.6" ry="6"/><path d="M1 7h12M2 4h10M2 10h10"/></g></svg>www.companyname.example</div>
  </address>
  <address class="contact-right">
    <div class="phone"><svg width="18" height="18" viewBox="0 0 24 24"><path fill="#fff" d="M6.6 10.8a15.1 15.1 0 0 0 6.6 6.6l2.2-2.2a1 1 0 0 1 1-.25 11.4 11.4 0 0 0 3.6.57 1 1 0 0 1 1 1V20a1 1 0 0 1-1 1A17 17 0 0 1 3 4a1 1 0 0 1 1-1h3.5a1 1 0 0 1 1 1c0 1.25.2 2.45.57 3.57a1 1 0 0 1-.25 1z"/></svg>(01) 555 014 273</div>
    <div class="address">Harbor lane 14, NY 10452</div>
  </address>
</main>
</body>
</html>
```